Looking for a creative label design for our retail coffee bags

We are a coffee manufacturer (coffee roaster) looking to re-brand our retail label for our coffee bags. Our main coffee blend that we sell is our Harborline Velvet Blend. You can use this name when creating the label. We are going for a look that represents our company as a coffee roaster. Please reference our website (www.brindlemugworks.com) and our Facebook page to learn more about our company and to give you more inspiration on creating this design.

Target Market(s)

Retail customers/grocery stores

Industry/Entity Type

Manufacturer

Requirements
Must have
• The size of the label has to be 3" width x 4" height

Logo must be Black
Nice to have
• We currently incorporate a color on our labels for each blend. For example, Harborline Velvet Blend (royal blue), Decaffeinated Blend (red), Breakfast Blend (green), Flavored coffees (gold).

Rustic/vintage style

```html
<!DOCTYPE html>
<html lang="en">
<head>
<meta charset="utf-8">
<title>Brindle Mugworks – Blend Labels</title>
<link href="https://fonts.googleapis.com/css2?family=Montserrat:wght@700;800&family=Roboto:wght@400&family=Roboto+Condensed:wght@400;700&family=Yellowtail&display=swap" rel="stylesheet">
<style>
  :root{
    --royal:#062464;
    --red:#f20d0d;
    --green:#3ab54a;
    --gold:#d1ac35;
    --ink:#111111;
    --paper:#ffffff;
  }
  *{box-sizing:border-box;margin:0;padding:0}
  html,body{width:1200px;height:1200px;overflow:hidden}
  body{
    position:relative;
    background:linear-gradient(180deg,#ffffff 0%,#ffffff 45%,#e2e2e2 100%);
    font-family:"Roboto",Arial,sans-serif;
  }
  .label{
    position:absolute;width:418px;height:560px;
    border:2px solid var(--accent);border-radius:26px;overflow:hidden;
    background:var(--accent);
    box-shadow:0 22px 16px -18px rgba(0,0,0,.35);
  }
  .label--supremo{left:39px;top:29px;--accent:var(--royal)}
  .label--decaf{left:532px;top:29px;--accent:var(--red)}
  .label--breakfast{left:39px;top:619px;--accent:var(--green)}
  .label--flavored{left:534px;top:619px;--accent:var(--gold)}

  .label__head{position:absolute;left:0;top:0;width:100%;height:184px;background:var(--paper)}
  .brand-rule{position:absolute;top:85px;height:2px;background:var(--ink)}
  .brand-rule--left{left:18px;width:110px}
  .brand-rule--right{right:18px;width:110px}
  .brand{
    position:absolute;left:50%;top:86px;transform:translate(-50%,-50%);
    display:flex;align-items:center;gap:6px;
    font-family:"Montserrat",sans-serif;font-weight:800;font-size:13px;
    color:var(--ink);letter-spacing:.04em;white-space:nowrap;
  }
  .brand__dot{width:12px;height:12px;border-radius:50%;background:var(--ink)}

  .label__title{
    position:absolute;left:0;top:196px;width:100%;text-align:center;
    font-family:"Montserrat",sans-serif;font-weight:700;font-size:29px;
    color:var(--paper);line-height:36px;white-space:nowrap;
  }
  .label--decaf .label__title{letter-spacing:.2em}
  .label--breakfast .label__title{letter-spacing:.22em}
  .label--flavored .label__title{letter-spacing:.08em}

  .title-rule{position:absolute;top:248px;height:2px;background:var(--paper);width:124px}
  .title-rule--left{left:18px}
  .title-rule--right{right:18px}
  .label__script{
    position:absolute;left:0;top:228px;width:100%;text-align:center;
    font-family:"Yellowtail",cursive;font-size:40px;line-height:44px;color:var(--paper);
  }

  .story{
    position:absolute;left:19px;top:284px;width:190px;
    color:var(--paper);font-size:8.6px;line-height:10.5px;text-align:justify;
  }
  .story p+p{margin-top:10px}

  .facts{position:absolute;left:229px;top:0;width:171px;color:var(--paper);text-align:center}
  .facts__years{position:absolute;top:283px;width:100%;font-family:"Montserrat",sans-serif;font-weight:800;font-size:42px;line-height:44px}
  .facts__line{position:absolute;width:100%;font-family:"Montserrat",sans-serif;font-weight:700;font-size:14px;line-height:16px}
  .facts__since{position:absolute;top:380px;left:38px;width:96px;height:30px}
  .facts__roast{position:absolute;top:422px;left:-6px;width:183px;font-family:"Roboto Condensed",sans-serif;font-size:13.5px;white-space:nowrap}
  .products{position:absolute;top:446px;left:2px;width:167px}
  .products__head{display:flex;align-items:center;gap:3px;font-family:"Montserrat",sans-serif;font-weight:800;font-size:8.5px;white-space:nowrap}
  .products__head::before,.products__head::after{content:"";flex:1;height:1.5px;background:var(--paper)}
  .products__list{list-style:none;margin-top:5px;font-family:"Roboto Condensed",sans-serif;font-size:19px;line-height:23px}
  .products__rule{height:2px;background:var(--paper);margin-top:4px}
</style>
</head>
<body>

<!-- Label template repeated per blend -->
<section class="label label--supremo">
  <div class="label__head">
    <span class="brand-rule brand-rule--left"></span>
    <div class="brand"><span class="brand__dot"></span>BRINDLE MUGWORKS</div>
    <span class="brand-rule brand-rule--right"></span>
  </div>
  <h2 class="label__title" style="font-size:27px">HARBORLINE VELVET</h2>
  <span class="title-rule title-rule--left"></span>
  <div class="label__script">Blend</div>
  <span class="title-rule title-rule--right"></span>
  <div class="story">
    <p>We started 20 years ago with nothing but an old roaster, small grinder, leaky roof and a wallet full of dreams. What we had that wasn't old or small was our coffee. It was big on quality and unique in its taste. From day one we roasted only the best obtainable Arabica beans, never mixing in inferior quality beans to keep our costs low.</p>
    <p>But just like a heap of new bricks and roofing shingles don't make a great looking house, the best beans on the market don't necessarily make excellent coffee. Our secret is our Harborline Velvet blend, or what our Master Blender and founder of Brindle Mugworks so proudly calls "Grandma's Secret Family Recipe". We spent countless smoky days roasting and brewing and then roasting again until we got it just right.</p>
    <p>Now we invite you to treat yourself with the very essence of our company, a pinnacle of 20 years of experience in finding the best beans and transmuting them into excellent coffee. They say a picture is worth a thousand words; our coffee is worth a thousand delicious sips and you will still be craving more.</p>
  </div>
  <div class="facts">
    <div class="facts__years">20</div>
    <div class="facts__line" style="top:323px">YEARS</div>
    <div class="facts__line" style="top:340px">OF</div>
    <div class="facts__line" style="top:358px">EXPERIENCE</div>
    <svg class="facts__since" viewBox="0 0 96 30"><line x1="30" y1="0" x2="66" y2="30" stroke="#fff" stroke-width="1.2"/><line x1="66" y1="0" x2="30" y2="30" stroke="#fff" stroke-width="1.2"/><text x="0" y="18" fill="#fff" font-family="Roboto,sans-serif" font-size="8">SINCE</text><text x="72" y="19" fill="#fff" font-family="Roboto,sans-serif" font-size="9.5">1994</text></svg>
    <div class="facts__roast">PROUDLY ROASTED IN MILLBROOK</div>
    <div class="products">
      <div class="products__head">OTHER PRODUCT</div>
      <ul class="products__list"><li>DECAFFEINATED BLEND</li><li>BREAKFAST BLEND</li><li>FLAVORED COFFEES</li></ul>
      <div class="products__rule"></div>
    </div>
  </div>
</section>

<section class="label label--decaf">
  <div class="label__head">
    <span class="brand-rule brand-rule--left"></span>
    <div class="brand"><span class="brand__dot"></span>BRINDLE MUGWORKS</div>
    <span class="brand-rule brand-rule--right"></span>
  </div>
  <h2 class="label__title">DECAFFEINATED</h2>
  <span class="title-rule title-rule--left"></span>
  <div class="label__script">Blend</div>
  <span class="title-rule title-rule--right"></span>
  <div class="story">
    <p>We started 20 years ago with nothing but an old roaster, small grinder, leaky roof and a wallet full of dreams. What we had that wasn't old or small was our coffee. It was big on quality and unique in its taste. From day one we roasted only the best obtainable Arabica beans, never mixing in inferior quality beans to keep our costs low.</p>
    <p>But just like a heap of new bricks and roofing shingles don't make a great looking house, the best beans on the market don't necessarily make excellent coffee. Our secret is our Harborline Velvet blend, or what our Master Blender and founder of Brindle Mugworks so proudly calls "Grandma's Secret Family Recipe". We spent countless smoky days roasting and brewing and then roasting again until we got it just right.</p>
    <p>Now we invite you to treat yourself with the very essence of our company, a pinnacle of 20 years of experience in finding the best beans and transmuting them into excellent coffee. They say a picture is worth a thousand words; our coffee is worth a thousand delicious sips and you will still be craving more.</p>
  </div>
  <div class="facts">
    <div class="facts__years">20</div>
    <div class="facts__line" style="top:323px">YEARS</div>
    <div class="facts__line" style="top:340px">OF</div>
    <div class="facts__line" style="top:358px">EXPERIENCE</div>
    <svg class="facts__since" viewBox="0 0 96 30"><line x1="30" y1="0" x2="66" y2="30" stroke="#fff" stroke-width="1.2"/><line x1="66" y1="0" x2="30" y2="30" stroke="#fff" stroke-width="1.2"/><text x="0" y="18" fill="#fff" font-family="Roboto,sans-serif" font-size="8">SINCE</text><text x="72" y="19" fill="#fff" font-family="Roboto,sans-serif" font-size="9.5">1994</text></svg>
    <div class="facts__roast">PROUDLY ROASTED IN MILLBROOK</div>
    <div class="products">
      <div class="products__head">OTHER PRODUCT</div>
      <ul class="products__list"><li>DECAFFEINATED BLEND</li><li>BREAKFAST BLEND</li><li>FLAVORED COFFEES</li></ul>
      <div class="products__rule"></div>
    </div>
  </div>
</section>

<section class="label label--breakfast">
  <div class="label__head">
    <span class="brand-rule brand-rule--left"></span>
    <div class="brand"><span class="brand__dot"></span>BRINDLE MUGWORKS</div>
    <span class="brand-rule brand-rule--right"></span>
  </div>
  <h2 class="label__title">BREAKFAST</h2>
  <span class="title-rule title-rule--left"></span>
  <div class="label__script">Blend</div>
  <span class="title-rule title-rule--right"></span>
  <div class="story">
    <p>We started 20 years ago with nothing but an old roaster, small grinder, leaky roof and a wallet full of dreams. What we had that wasn't old or small was our coffee. It was big on quality and unique in its taste. From day one we roasted only the best obtainable Arabica beans, never mixing in inferior quality beans to keep our costs low.</p>
    <p>But just like a heap of new bricks and roofing shingles don't make a great looking house, the best beans on the market don't necessarily make excellent coffee. Our secret is our Harborline Velvet blend, or what our Master Blender and founder of Brindle Mugworks so proudly calls "Grandma's Secret Family Recipe". We spent countless smoky days roasting and brewing and then roasting again until we got it just right.</p>
    <p>Now we invite you to treat yourself with the very essence of our company, a pinnacle of 20 years of experience in finding the best beans and transmuting them into excellent coffee. They say a picture is worth a thousand words; our coffee is worth a thousand delicious sips and you will still be craving more.</p>
  </div>
  <div class="facts">
    <div class="facts__years">20</div>
    <div class="facts__line" style="top:323px">YEARS</div>
    <div class="facts__line" style="top:340px">OF</div>
    <div class="facts__line" style="top:358px">EXPERIENCE</div>
    <svg class="facts__since" viewBox="0 0 96 30"><line x1="30" y1="0" x2="66" y2="30" stroke="#fff" stroke-width="1.2"/><line x1="66" y1="0" x2="30" y2="30" stroke="#fff" stroke-width="1.2"/><text x="0" y="18" fill="#fff" font-family="Roboto,sans-serif" font-size="8">SINCE</text><text x="72" y="19" fill="#fff" font-family="Roboto,sans-serif" font-size="9.5">1994</text></svg>
    <div class="facts__roast">PROUDLY ROASTED IN MILLBROOK</div>
    <div class="products">
      <div class="products__head">OTHER PRODUCT</div>
      <ul class="products__list"><li>DECAFFEINATED BLEND</li><li>BREAKFAST BLEND</li><li>FLAVORED COFFEES</li></ul>
      <div class="products__rule"></div>
    </div>
  </div>
</section>

<section class="label label--flavored">
  <div class="label__head">
    <span class="brand-rule brand-rule--left"></span>
    <div class="brand"><span class="brand__dot"></span>BRINDLE MUGWORKS</div>
    <span class="brand-rule brand-rule--right"></span>
  </div>
  <h2 class="label__title">FLAVORED COFFEES</h2>
  <span class="title-rule title-rule--left"></span>
  <div class="label__script">Blend</div>
  <span class="title-rule title-rule--right"></span>
  <div class="story">
    <p>We started 20 years ago with nothing but an old roaster, small grinder, leaky roof and a wallet full of dreams. What we had that wasn't old or small was our coffee. It was big on quality and unique in its taste. From day one we roasted only the best obtainable Arabica beans, never mixing in inferior quality beans to keep our costs low.</p>
    <p>But just like a heap of new bricks and roofing shingles don't make a great looking house, the best beans on the market don't necessarily make excellent coffee. Our secret is our Harborline Velvet blend, or what our Master Blender and founder of Brindle Mugworks so proudly calls "Grandma's Secret Family Recipe". We spent countless smoky days roasting and brewing and then roasting again until we got it just right.</p>
    <p>Now we invite you to treat yourself with the very essence of our company, a pinnacle of 20 years of experience in finding the best beans and transmuting them into excellent coffee. They say a picture is worth a thousand words; our coffee is worth a thousand delicious sips and you will still be craving more.</p>
  </div>
  <div class="facts">
    <div class="facts__years">20</div>
    <div class="facts__line" style="top:323px">YEARS</div>
    <div class="facts__line" style="top:340px">OF</div>
    <div class="facts__line" style="top:358px">EXPERIENCE</div>
    <svg class="facts__since" viewBox="0 0 96 30"><line x1="30" y1="0" x2="66" y2="30" stroke="#fff" stroke-width="1.2"/><line x1="66" y1="0" x2="30" y2="30" stroke="#fff" stroke-width="1.2"/><text x="0" y="18" fill="#fff" font-family="Roboto,sans-serif" font-size="8">SINCE</text><text x="72" y="19" fill="#fff" font-family="Roboto,sans-serif" font-size="9.5">1994</text></svg>
    <div class="facts__roast">PROUDLY ROASTED IN MILLBROOK</div>
    <div class="products">
      <div class="products__head">OTHER PRODUCT</div>
      <ul class="products__list"><li>DECAFFEINATED BLEND</li><li>BREAKFAST BLEND</li><li>FLAVORED COFFEES</li></ul>
      <div class="products__rule"></div>
    </div>
  </div>
</section>

</body>
</html>
```